Business Card Design Project

I am a Homoeopath and would like a new business card which represents my clinic and how I work...My clinic Thistle Wellness is situated near Calderwood forest, you can hear the lyrebirds calling all the time!
My work is holistic and deals with shifting energy in order to create balance within the body. There is a very strong spiritual element to my work.
I have uploaded my current card, As far as the actual details on the front and the back I would like these to remain in the same structure...

Target Market(s)

those looking for alternative health therapies... all of my patients are referred to me so I am not concerned about fitting into a mainstream box

Industry/Entity Type

Clinic

Requirements
Must have
• This card must not look corporate!
be creative and different

Nice to have
• I am picturing a tree of life with roots heading into the earth and on it is a white peacock, maybe a body of water and a full moon nearby?

```html
<!DOCTYPE html>
<html lang="en">
<head>
<meta charset="utf-8">
<title>Thistle Wellness — Business Card</title>
<link rel="stylesheet" href="https://fonts.googleapis.com/css2?family=Arimo:wght@400;700&family=Questrial&display=swap">
<style>
  :root {
    --stage: #2b211b;
    --plum-deep: #3a1050;
    --plum-dark: #4a1766;
    --violet: #7b37a6;
    --violet-light: #9a55c4;
    --rose: #a0478a;
    --rose-light: #c47aad;
    --rose-pale: #d79cc4;
    --white: #ffffff;
    --card-w: 560px;
    --card-h: 330px;
  }
  * { margin: 0; padding: 0; box-sizing: border-box; }
  html, body { width: 1200px; height: 900px; overflow: hidden; }
  body {
    background: var(--stage);
    position: relative;
    font-family: "Arimo", Arial, sans-serif;
    color: var(--white);
  }
  .showcase-title {
    position: absolute;
    right: 55px;
    top: 30px;
    font-family: "Questrial", sans-serif;
    font-size: 52px;
    font-weight: 400;
    color: var(--white);
  }
  .card {
    position: absolute;
    width: var(--card-w);
    height: var(--card-h);
    border-radius: 26px;
    overflow: hidden;
    box-shadow: 0 14px 30px rgba(0,0,0,0.45);
  }
  .ripple-artwork {
    position: absolute;
    border-radius: 50%;
  }
  .brand-name {
    position: absolute;
    font-family: "Questrial", sans-serif;
    color: var(--white);
    display: flex;
    align-items: center;
    gap: 10px;
    white-space: nowrap;
  }
  .brand-dot {
    display: inline-block;
    border-radius: 50%;
    background: var(--white);
  }

  /* Appointment card */
  .appointment-card {
    left: 60px; top: 150px;
    background: linear-gradient(100deg, var(--rose) 0%, var(--rose-light) 55%, var(--rose-pale) 75%, var(--rose) 100%);
  }
  .appointment-card .ripple-artwork {
    left: -60px; top: 20px; width: 240px; height: 170px;
    background: radial-gradient(ellipse at 40% 50%, rgba(90,28,116,0.85) 0%, rgba(62,18,85,0.6) 55%, rgba(62,18,85,0) 75%);
  }
  .appointment-card .brand-name { left: 36px; top: 214px; font-size: 19px; }
  .appointment-card .brand-dot { width: 13px; height: 13px; }
  .appointment-heading {
    position: absolute; left: 220px; top: 48px;
    font-size: 19px; font-weight: 700;
  }
  .appointment-lines { position: absolute; left: 220px; top: 80px; }
  .appointment-line {
    width: 320px; height: 36px; background: var(--white);
    margin-bottom: 9px;
  }
  .appointment-footer {
    position: absolute; left: 0; right: 0; bottom: 0; height: 66px;
    background: linear-gradient(90deg, var(--plum-deep), var(--plum-dark) 60%, var(--rose) 100%);
    padding: 13px 40px;
    font-size: 16px; line-height: 20px;
  }

  /* Business card */
  .business-card {
    left: 580px; top: 420px;
    background: linear-gradient(90deg, var(--plum-deep) 0%, var(--plum-dark) 45%, var(--violet) 70%, var(--violet-light) 85%, var(--violet) 100%);
  }
  .business-card .ripple-artwork {
    left: 370px; top: 30px; width: 260px; height: 230px;
    background: radial-gradient(ellipse at 55% 50%, rgba(200,139,230,0.55) 0%, rgba(176,112,214,0.35) 50%, rgba(176,112,214,0) 72%);
  }
  .business-card .brand-name { left: 50px; top: 76px; font-size: 30px; }
  .business-card .brand-dot { width: 18px; height: 18px; }
  .contact-band {
    position: absolute; left: 0; right: 0; top: 165px; height: 125px;
    background: linear-gradient(90deg, var(--rose) 0%, var(--rose-light) 60%, rgba(196,122,173,0.1) 100%);
    padding: 14px 40px;
  }
  .practitioner { font-size: 22px; font-weight: 700; }
  .practitioner .role { font-size: 15px; font-weight: 400; }
  .credentials { font-size: 15px; margin-top: 2px; }
  .contact { font-size: 17px; line-height: 20px; margin-top: 16px; }
</style>
</head>
<body>
  <div class="showcase-title">Thistle Wellness</div>

  <section class="card appointment-card">
    <div class="ripple-artwork" role="img" aria-label="Decorative ripple artwork in deep purple"></div>
    <div class="brand-name"><span class="brand-dot"></span>Thistle Wellness</div>
    <div class="appointment-heading">Your next appointment</div>
    <div class="appointment-lines">
      <div class="appointment-line"></div>
      <div class="appointment-line"></div>
      <div class="appointment-line"></div>
    </div>
    <div class="appointment-footer">
      27 Fernhill Road, Oakvale.<br>03 5900 4172
    </div>
  </section>

  <section class="card business-card">
    <div class="ripple-artwork" role="img" aria-label="Decorative ripple artwork in light violet"></div>
    <div class="brand-name"><span class="brand-dot"></span>Thistle Wellness</div>
    <div class="contact-band">
      <div class="practitioner">Maren Ellsworth <span class="role">| Classical Homeopath</span></div>
      <div class="credentials">Ad Dip Hom Prof Memb CHA Aroh Regd</div>
      <div class="contact">maren.ellsworth@fernmail.com<br>0400 318 262</div>
    </div>
  </section>
</body>
</html>
```